Modern corporate energy/fuel business need business card design

Business card required for company founder. Halden Fuel Systems is a Australian based modern energy/fuel provider. We offer specialised solutions to businesses using fossil fuels through renewable energy solutions.

I would like one side with specific information (name, address etc)

The other side to be bold, professional company name & logo. Striking.

Target Market(s)

B2B. Transport, mining, councils, environmentalist,

Industry/Entity Type

Petroleum

Contact Information for Business Card

Name; Peter Morrow
Position; Director
Email; pmorrow@haldenfuel.com.au
Address; PO Box 347, Marrick, QLD, 4890
Website; www.haldenfuel.com.au

Colors

Designer to choose colors to be used in the design.

Requirements
Must have
• Clean, easy to read, professional & strong theme
Should not have
• too many colours, busy layout,

```html
<!DOCTYPE html>
<html lang="en">
<head>
<meta charset="utf-8">
<title>Halden Fuel Systems – Business Card</title>
<link href="https://fonts.googleapis.com/css2?family=Open+Sans:wght@400;600;700&display=swap" rel="stylesheet">
<style>
  :root {
    --navy: #2a5680;
    --orange: #f0701e;
    --orange-soft: #f4a36e;
    --ink: #3a3f47;
    --card: #ffffff;
    --backdrop: #e9ebee;
    --rule: #9aa3ad;
  }
  * { margin: 0; padding: 0; box-sizing: border-box; }
  html, body { width: 1200px; height: 900px; overflow: hidden; }
  body {
    background: var(--backdrop);
    font-family: "Open Sans", Arial, sans-serif;
    position: relative;
  }
  .card {
    position: absolute;
    left: 250px;
    width: 700px;
    height: 400px;
    background: var(--card);
    border-radius: 22px;
    overflow: hidden;
    box-shadow: 0 6px 20px rgba(20, 30, 45, 0.15);
  }
  .card--brand { top: 40px; }
  .card--contact { top: 470px; }

  .band { position: absolute; left: 0; width: 700px; }
  .card--brand .band { top: 292px; height: 60px; }
  .card--contact .band { top: 318px; height: 50px; }

  /* Brand side */
  .company-name {
    position: absolute; top: 130px; left: 0; width: 700px;
    text-align: center;
    color: var(--navy); font-weight: 700; font-size: 50px; line-height: 1;
    white-space: nowrap;
  }
  .band-web {
    position: absolute; top: 304px; left: 228px; width: 250px;
    color: #fff; font-size: 15px; letter-spacing: 1.5px; text-align: center;
    white-space: nowrap;
  }

  /* Contact side */
  .person { position: absolute; top: 48px; left: 62px; }
  .person-name { color: var(--navy); font-size: 26px; font-weight: 700; letter-spacing: 1px; }
  .person-role { color: var(--orange-soft); font-size: 14px; letter-spacing: 1px; margin-top: 2px; }
  .connector { position: absolute; top: 0; left: 0; }
  .contact-list { position: absolute; top: 132px; left: 62px; list-style: none; }
  .contact-list li {
    display: flex; align-items: center; gap: 12px;
    color: var(--ink); font-size: 15px; line-height: 28px;
  }
  .contact-list svg { width: 14px; height: 14px; flex: none; }
  .contact-company {
    position: absolute; top: 232px; left: 390px;
    color: var(--navy); font-weight: 700; font-size: 26px; line-height: 1;
    white-space: nowrap;
  }
  .address {
    position: absolute; top: 330px; left: 34px;
    color: #fff; font-size: 15px; white-space: nowrap;
  }
  .social {
    position: absolute; top: 330px; left: 372px;
    display: flex; align-items: center; gap: 12px;
    color: #fff; font-size: 16px; white-space: nowrap;
  }
  .social-square { width: 18px; height: 18px; background: var(--orange); border-radius: 3px; }
</style>
</head>
<body>

<section class="card card--brand" aria-label="Brand side">
  <div class="company-name">Halden Fuel Systems</div>
  <svg class="band" viewBox="0 0 700 60" aria-hidden="true">
    <polygon points="0,0 190,0 170,26 0,26" fill="var(--orange)"/>
    <polygon points="200,6 500,6 478,46 172,46" fill="var(--navy)"/>
    <polygon points="508,26 700,26 700,60 488,60" fill="var(--orange)"/>
  </svg>
  <div class="band-web">www.haldenfuel.com.au</div>
</section>

<section class="card card--contact" aria-label="Contact side">
  <div class="person">
    <div class="person-name">PETER MORROW</div>
    <div class="person-role">DIRECTOR</div>
  </div>
  <svg class="connector" width="700" height="400" aria-hidden="true">
    <line x1="62" y1="112" x2="200" y2="112" stroke="var(--rule)" stroke-width="1"/>
    <line x1="200" y1="112" x2="378" y2="245" stroke="var(--rule)" stroke-width="1"/>
    <circle cx="378" cy="245" r="2" fill="var(--navy)"/>
  </svg>
  <ul class="contact-list">
    <li>
      <svg viewBox="0 0 14 14"><path d="M3 1 L5.5 1 L6.5 4 L5 5.2 C5.8 7 7 8.2 8.8 9 L10 7.5 L13 8.5 L13 11 C13 12 12 13 11 13 C5.5 12.5 1.5 8.5 1 3 C1 2 2 1 3 1 Z" fill="var(--navy)"/></svg>
      0000 000 00
    </li>
    <li>
      <svg viewBox="0 0 14 14"><rect x="1" y="3" width="12" height="8.5" rx="1" fill="var(--navy)"/><path d="M1.5 3.5 L7 8 L12.5 3.5" stroke="#fff" stroke-width="1" fill="none"/></svg>
      pmorrow@haldenfuel.com.au
    </li>
    <li>
      <svg viewBox="0 0 14 14"><circle cx="7" cy="7" r="6" fill="none" stroke="var(--navy)" stroke-width="1.3"/><ellipse cx="7" cy="7" rx="2.6" ry="6" fill="none" stroke="var(--navy)" stroke-width="1"/><line x1="1" y1="7" x2="13" y2="7" stroke="var(--navy)" stroke-width="1"/></svg>
      www.haldenfuel.com.au
    </li>
  </ul>
  <div class="contact-company">Halden Fuel Systems</div>
  <svg class="band" viewBox="0 0 700 50" aria-hidden="true">
    <polygon points="0,0 345,0 320,50 0,50" fill="var(--orange)"/>
    <polygon points="352,0 700,0 700,50 327,50" fill="var(--navy)"/>
  </svg>
  <div class="address">PO Box 347, Marrick, QLD, 4890</div>
  <div class="social">
    <span>HaldenFuelSystems/</span>
    <span class="social-square"></span>
  </div>
</section>

</body>
</html>
```